Business Card Design and Logo Needed

I need Business Cards and a Logo for my website and public speaking business which can be found at: www.kelsa-thorn.example

I'm looking for creative and unique ideas. Some business cards I've found online that I like can be found at:
http://gigplatelo.example/general/18-smokin-hot-business-card-designs/

and at

http://www.vortaplume.example/2009/04/50-creative-business-cards-of-50-graphic-designers/

```html
<!DOCTYPE html>
<html lang="en">
<head>
<meta charset="utf-8">
<title>Kelsa Thorn – Business Card</title>
<link rel="stylesheet" href="https://fonts.googleapis.com/css2?family=Allura&family=Didact+Gothic&display=swap">
<style>
  :root {
    --ink: #000000;
    --paper: #ffffff;
    --accent-red: #e0191e;
    --clip-tone: #d9d9d9;
  }
  html, body {
    margin: 0;
    padding: 0;
    width: 1200px;
    height: 1001px;
    overflow: hidden;
    background: var(--paper);
  }
  .card-canvas {
    display: block;
    width: 1200px;
    height: 1001px;
  }
  .card-outline {
    fill: var(--paper);
    stroke: var(--ink);
    stroke-width: 9;
    stroke-linejoin: round;
  }
  .ruled-line {
    stroke: var(--ink);
    stroke-width: 5;
    stroke-linecap: round;
  }
  .margin-line {
    stroke: var(--accent-red);
    stroke-width: 5;
    stroke-linecap: round;
  }
  .binder-clip {
    fill: var(--clip-tone);
  }
  .owner-name {
    font-family: "Allura", cursive;
    font-size: 104px;
    fill: var(--ink);
  }
  .owner-role {
    font-family: "Didact Gothic", sans-serif;
    font-size: 39px;
    fill: var(--ink);
  }
  .contact-line {
    font-family: "Didact Gothic", sans-serif;
    font-size: 35px;
    fill: var(--ink);
  }
</style>
</head>
<body>
<svg class="card-canvas" viewBox="0 0 1200 1001" xmlns="http://www.w3.org/2000/svg">
  <!-- card body -->
  <polygon class="card-outline" points="23,208 1165,182 1152,946 38,969"/>

  <!-- header -->
  <text class="owner-name" x="1120" y="312" text-anchor="end">Kelsa Thorn</text>
  <text class="owner-role" x="1127" y="380" text-anchor="end">Speaker, Philanthropist, Author</text>

  <!-- ruled lines -->
  <line class="margin-line" x1="30" y1="412" x2="1150" y2="398"/>
  <line class="ruled-line" x1="32" y1="476" x2="1150" y2="468"/>
  <line class="ruled-line" x1="32" y1="548" x2="1150" y2="540"/>
  <line class="ruled-line" x1="33" y1="619" x2="1150" y2="612"/>
  <line class="ruled-line" x1="34" y1="694" x2="1150" y2="686"/>
  <line class="ruled-line" x1="35" y1="765" x2="1150" y2="758"/>
  <line class="ruled-line" x1="36" y1="840" x2="1150" y2="832"/>

  <!-- contact details -->
  <text class="contact-line" x="1123" y="506" text-anchor="end">www.kelsa-thorn.example</text>
  <text class="contact-line" x="1123" y="578" text-anchor="end">www.friendvista.example/ImKelsaThorn</text>
  <text class="contact-line" x="1123" y="650" text-anchor="end">www.chirpline.example/imkelsathorn</text>
  <text class="contact-line" x="1123" y="722" text-anchor="end">www.kelsa-thorn.blogpage.example</text>
  <text class="contact-line" x="1123" y="794" text-anchor="end">info@kelsa-thorn.example</text>

  <!-- binder clip holding the card -->
  <rect class="binder-clip" x="100" y="12" width="266" height="314" rx="18" role="img" aria-label="Binder clip clamped over the top left of the card"/>
</svg>
</body>
</html>
```